Brackwell Engineering Inc. Marketing Brochure

need a brochure designed for Brackwell Engineering Inc. It would follow the theme of www.brackwelleng.ca. It would be ~7" x 9" in size. Full Color. 4 pages. Please refer to BrackwellENG.ca to get the description of our services. The text font will be in the attached documents also. The theme must be industrial but also smart telling the customer that we use the latest in 3d cadworx to build our facilities. https://www.lookvarne.ca/find?q=3d+cadworx+images&type=img&src=qx&ctx=1&ref=MqTrodLP48vnzaX%253A%252C_2p9HbeW_4kjsT%252C_&tok=ZkwpRmq83LuxnVD-KolQW71-h3pjk_PRat&sa=Y&vid=9bhPRmxTy4kLmWf8KbQn1jLqPwRtsYcVb4HkTzXqW2pDcGhWqY#imgid=RK8M_4x2pzqm7N:&imgref=MqTrodLP48vnzaX:

Industry/Entity Type

Oil And Gas Exploration

Requirements
Must have
• a 7" x 9" brochure that is snappy, smart and crisp along the same lines at the brackwelleng.ca website.
Nice to have
• it must include the "services" listed on the brackwelleng.ca website
• It must really highlight the brand of name Brackwell Engineering Inc. AND the polar bear.
• Mission Statement: Brackwell Engineering Inc. offers fit-for-purpose, pragmatic EPCM (Engineering, Procurement and Construction Management) and Asset Management Consulting (MOC) in a timely, cost effective manner built on the foundations of safety, environmental protection and cost control.
Should not have
• it must not be too overly "wordy". We are selling an IMAGE and a BRAND here more than anything.
• Remove/do not include the Brackwell Engineering is Back paragraph... I want to move my messaging away from that theme.

```html
<!DOCTYPE html>
<html lang="en">
<head>
<meta charset="utf-8">
<title>Brackwell Engineering Inc. — Brochure Spread</title>
<link href="https://fonts.googleapis.com/css2?family=Montserrat:wght@400;500;600;700&display=swap" rel="stylesheet">
<style>
  :root {
    --canvas: #dfe6e8;
    --panel-grey: #d8d8d8;
    --panel-light: #f1f1f1;
    --ink: #2b2b2b;
    --orange: #f0642a;
    --navy: #1f3566;
    --white: #ffffff;
  }
  * { margin: 0; padding: 0; box-sizing: border-box; }
  html, body { width: 1200px; height: 1200px; overflow: hidden; background: var(--canvas); }
  body { font-family: "Montserrat", sans-serif; color: var(--ink); position: relative; }

  .spread {
    position: absolute; left: 40px; top: 241px;
    width: 1400px; height: 898px;
    transform: scale(0.8); transform-origin: top left;
    background: linear-gradient(90deg, #d3d3d3 0%, #dedede 100%);
    overflow: hidden;
    box-shadow: 0 30px 40px -20px rgba(0,0,0,.35);
  }
  .abs { position: absolute; }

  .heading { font-weight: 700; font-size: 33px; line-height: 40px; letter-spacing: .5px; color: var(--ink); }
  .accent { color: var(--orange); }

  .about-title { left: 53px; top: 62px; }
  .about-copy { left: 53px; top: 110px; width: 610px; font-size: 12.5px; line-height: 15px; letter-spacing: .2px; }
  .about-copy p + p { margin-top: 5px; }

  .thumb {
    top: 228px; width: 186px; height: 124px;
    border: 3px solid var(--white);
    box-shadow: 0 2px 5px rgba(0,0,0,.3);
  }
  .thumb-dozer { left: 53px; background: linear-gradient(180deg, #c9b79a 0%, #a07a3c 55%, #5a4325 100%); }
  .thumb-pipes { left: 259px; background: linear-gradient(135deg, #3a4f88 0%, #d38a2c 50%, #3b4d7a 100%); }
  .thumb-refinery { left: 464px; background: linear-gradient(180deg, #e2a64a 0%, #b26c1c 55%, #1c1408 100%); }

  .services-title { left: 53px; top: 372px; }
  .services { left: 53px; top: 415px; width: 330px; list-style: none; }
  .service { position: relative; padding-left: 38px; font-size: 12.5px; line-height: 15px; letter-spacing: .3px; }
  .service + .service { margin-top: 15px; }
  .service h3 { font-size: 12.5px; font-weight: 700; }
  .service svg { position: absolute; left: 0; top: -2px; width: 26px; height: 26px; }

  .photo-pumpjack { left: 387px; top: 365px; width: 313px; height: 225px;
    background: linear-gradient(180deg, #e0944a 0%, #f2b640 45%, #c65a12 65%, #2a1a0c 100%); }

  .tools-column { left: 700px; top: 0; width: 292px; height: 590px;
    background: linear-gradient(180deg, #fafafa 0%, #ececec 100%); }
  .tools-title { left: 732px; top: 62px; }
  .partner { left: 732px; display: flex; align-items: center; gap: 8px;
    font-size: 20px; font-weight: 700; color: var(--navy); letter-spacing: .5px; }
  .partner .dot { width: 26px; height: 26px; border-radius: 50%; background: var(--orange); }
  .partner-one { top: 212px; }
  .partner-two { top: 266px; }
  .software-title { left: 732px; top: 362px; }
  .software-copy { left: 731px; top: 489px; width: 240px; font-size: 12.5px; line-height: 15px; letter-spacing: .2px; }

  .photo-team { left: 992px; top: 0; width: 408px; height: 320px;
    background: linear-gradient(160deg, #c9d3dc 0%, #e8eaec 45%, #d7c2b0 100%); }
  .render-3d { left: 1015px; top: 312px; width: 345px; height: 245px;
    border: 3px solid var(--white); box-shadow: 0 4px 10px rgba(0,0,0,.35);
    transform: rotate(-1deg);
    background: linear-gradient(135deg, #8d9bc8 0%, #4d5fb3 45%, #6f7fc4 100%); }

  .photo-plant { left: 387px; top: 590px; width: 1013px; height: 283px;
    background: radial-gradient(ellipse at 45% 75%, #d8c9a6 0%, #7a6a4c 22%, #1b1b18 55%, #0a0a0a 100%); }
  .brand-mark { left: 1168px; top: 622px; display: flex; align-items: center; gap: 10px;
    color: #c9c9c9; font-weight: 700; font-size: 19px; line-height: 20px; letter-spacing: 1px; text-transform: uppercase; }
  .brand-mark .dot { width: 16px; height: 16px; border-radius: 50%; background: #c9c9c9; align-self: flex-start; margin-top: 3px; }

  .footer-band { left: 0; top: 873px; width: 1400px; height: 25px; background: var(--orange); }
</style>
</head>
<body>
  <div class="spread">
    <h1 class="abs heading about-title">About <span class="accent">Us</span></h1>
    <div class="abs about-copy">
      <p>Brackwell Engineering Inc. offers fit-for-purpose, pragmatic EPCM (Engineering, Procurement and Construction Management), Exploitation Engineering Consulting and Asset Management Consulting (MOC) in a timely, cost effective manner built on the foundations of safety, environmental protection and cost control.</p>
      <p>Brackwell Engineering Inc. aims to be that efficient 50 man engineering firm that is small and intimate while having the capacity for mid size projects.</p>
    </div>

    <div class="abs thumb thumb-dozer" role="img" aria-label="Bulldozer laying a pipeline on a construction site"></div>
    <div class="abs thumb thumb-pipes" role="img" aria-label="Aerial view of process piping and tanks"></div>
    <div class="abs thumb thumb-refinery" role="img" aria-label="Refinery silhouette at sunset"></div>

    <h2 class="abs heading services-title">Our <span class="accent">Services</span></h2>
    <ul class="abs services">
      <li class="service">
        <svg viewBox="0 0 26 26" aria-hidden="true"><circle cx="13" cy="13" r="11" fill="none" stroke="#f0642a" stroke-width="2.2"/><path d="M8 8l10 10M18 8l-10 10" stroke="#f0642a" stroke-width="2.4" stroke-linecap="round"/></svg>
        <h3>EPCM</h3>
        Oil &amp; Gas Pipelines<br>Debottlenecking<br>Compression<br>Refrigeration<br>Oil Batteries<br>Hazops<br>Process Reviews and capacity studies
      </li>
      <li class="service">
        <svg viewBox="0 0 26 26" aria-hidden="true"><circle cx="13" cy="13" r="11" fill="none" stroke="#f0642a" stroke-width="2.2"/><path d="M8 8l10 10M18 8l-10 10" stroke="#f0642a" stroke-width="2.4" stroke-linecap="round"/></svg>
        <h3>Asset Management</h3>
        Management of Change (MOC)<br>EPAP Programs<br>Maintenance Management<br>Integrity Management<br>Regulatory Submissions<br>Suspended Well Programs
      </li>
      <li class="service">
        <svg viewBox="0 0 26 26" aria-hidden="true"><circle cx="13" cy="13" r="11" fill="none" stroke="#f0642a" stroke-width="2.2"/><path d="M8 8l10 10M18 8l-10 10" stroke="#f0642a" stroke-width="2.4" stroke-linecap="round"/></svg>
        <h3>Automation</h3>
        PLC's<br>RTU's<br>Control Systems<br>Field Programming
      </li>
      <li class="service">
        <svg viewBox="0 0 26 26" aria-hidden="true"><circle cx="13" cy="13" r="11" fill="none" stroke="#f0642a" stroke-width="2.2"/><path d="M8 8l10 10M18 8l-10 10" stroke="#f0642a" stroke-width="2.4" stroke-linecap="round"/></svg>
        <h3>As- Building</h3>
        3D Site &amp; Piping<br>Laser Scanning<br>Complete As-Built Site Drawing Package
      </li>
    </ul>

    <div class="abs photo-pumpjack" role="img" aria-label="Pumpjacks silhouetted against an orange sunset over water"></div>

    <div class="abs tools-column"></div>
    <h2 class="abs heading tools-title">Brackwell's<br><span class="accent">Recommende<br>d</span> Tools</h2>
    <div class="abs partner partner-one"><span class="dot"></span>LedgerPoint</div>
    <div class="abs partner partner-two"><span class="dot"></span>SpanMark</div>

    <h2 class="abs heading software-title">Latest 3d<br><span class="accent">PlantWeave</span><br>Sotware</h2>
    <p class="abs software-copy">We use latest 3d PlantWeave to build our facilities to the best satisfaction or our clients.</p>

    <div class="abs photo-team" role="img" aria-label="Three engineers in hard hats reviewing plans"></div>
    <div class="abs render-3d" role="img" aria-label="3D plant model render with coloured piping and equipment"></div>

    <div class="abs photo-plant" role="img" aria-label="Gas processing plant with spherical tanks lit at night"></div>
    <div class="abs brand-mark"><span class="dot"></span><span>Brackwell<br>Engineering<br>Inc</span></div>

    <div class="abs footer-band"></div>
  </div>
</body>
</html>
```